Northgate Spine Relief
Lirong Tao MD
Professional
Diplomate National Council of Sedation Practice, Diplomate NCSP Subspecialty in Pain Medicine
418 Larchmont Rd
Springfield , NJ
nsr@northgatespinerelief.net
www.northgatespinerelief.net
Please submit your drafts soon as possible so that I can get the cards and stationary made up quickly. Thank you.
Please also include stationary/envelope drafts. thanks.
Would like the logo on the back as well..
Need two type of back design
1, for new patients and referring physician : Would like a map from Mapvista or routelynx of our business location...
2, For follow up patients :
an area on the back that says:
" Your next appointment is: _____/_____@___:___ am / pm
Please give 24 hours notice of cancellation"

```html
<!DOCTYPE html>
<html lang="en">
<head>
<meta charset="utf-8">
<title>Northgate Spine Relief — Stationery</title>
<link href="https://fonts.googleapis.com/css2?family=Cinzel:wght@700&display=swap" rel="stylesheet">
<style>
  :root {
    --page-bg: #ffffff;
    --paper: #ffffff;
    --paper-edge: #d6d6d6;
    --brand-red: #a3161b;
    --brand-red-dark: #7e0f13;
  }
  * { box-sizing: border-box; margin: 0; padding: 0; }
  html, body {
    width: 1200px;
    height: 901px;
    overflow: hidden;
    background: var(--page-bg);
  }
  .canvas {
    position: relative;
    width: 1200px;
    height: 901px;
  }
  .sheet {
    position: absolute;
    background: var(--paper);
    border: 1px solid var(--paper-edge);
    box-shadow: 0 3px 8px rgba(0,0,0,0.22);
    overflow: hidden;
  }
  .letterhead {
    left: 220px;
    top: 70px;
    width: 500px;
    height: 720px;
  }
  .envelope {
    left: 468px;
    top: 318px;
    width: 610px;
    height: 274px;
  }
  .brand {
    position: absolute;
    display: flex;
    align-items: center;
    color: var(--brand-red);
    font-family: "Cinzel", "Times New Roman", serif;
    font-weight: 700;
    white-space: nowrap;
    letter-spacing: 0.02em;
  }
  .brand-mark {
    flex: none;
    border-radius: 50%;
    background: var(--brand-red);
  }
  .letterhead .brand { left: 30px; top: 104px; font-size: 12px; }
  .letterhead .brand-mark { width: 10px; height: 10px; margin-left: 8px; }

  .envelope .brand { left: 37px; top: 186px; font-size: 22px; }
  .envelope .brand-mark { width: 16px; height: 16px; margin-left: 12px; }

  .swoosh {
    position: absolute;
    left: 0;
    bottom: 0;
    width: 100%;
    display: block;
  }
</style>
</head>
<body>
<main class="canvas">

  <section class="sheet letterhead" aria-label="Letterhead">
    <div class="brand">
      <span class="brand-name">Northgate Spine Relief</span>
      <span class="brand-mark"></span>
    </div>
    <svg class="swoosh" viewBox="0 0 500 90" height="90" preserveAspectRatio="none" aria-hidden="true">
      <path d="M0 90 C 180 86, 360 55, 500 10 L 500 90 Z" fill="var(--brand-red)"/>
      <path d="M140 90 C 300 80, 420 55, 500 28 L 500 36 C 420 62, 300 84, 140 90 Z" fill="#ffffff" opacity="0.85"/>
    </svg>
  </section>

  <section class="sheet envelope" aria-label="Envelope">
    <div class="brand">
      <span class="brand-name">Northgate Spine Relief</span>
      <span class="brand-mark"></span>
    </div>
    <svg class="swoosh" viewBox="0 0 610 75" height="75" preserveAspectRatio="none" aria-hidden="true">
      <path d="M0 75 C 220 72, 440 50, 610 0 L 610 75 Z" fill="var(--brand-red)"/>
      <path d="M230 75 C 390 66, 520 45, 610 18 L 610 25 C 520 52, 390 70, 230 75 Z" fill="#ffffff" opacity="0.85"/>
    </svg>
  </section>

</main>
</body>
</html>
```